Roll Up Design Velumo

We are a beauty company and we need stunning design for our general roll-up banner that we gonna place just next to the main gate of mall that we are located in. The most important for us is the quality, accuracy and the unity of poster. It has to be super elegant, engaging and beautiful. Has to match our service standards (high). Colors do not matter as long as the overall look is exciting.
Examples and our logo are attached
Updates
Reason: We need more designs (more creativity, more quality, colurs and proportions).
Target Market(s)
Middle class ladies, students, business women
Industry/Entity Type
It Company
Colors
Designer to choose colors to be used in the design.
Look and feel
Each slider illustrates characteristics of the customer's brand and the style your logo design should communicate.

```html
<!DOCTYPE html>
<html lang="az">
<head>
<meta charset="utf-8">
<title>Velumo Gözəllik – Roll-up Banner</title>
<link href="https://fonts.googleapis.com/css2?family=Montserrat:wght@600;700&family=Questrial&display=swap" rel="stylesheet">
<style>
  :root {
    --page-bg: #ffffff;
    --banner-top: #b9c3cf;
    --banner-mid: #d6dde5;
    --banner-low: #c3ccd6;
    --ink: #111111;
    --band: #0c0c0c;
    --band-sheen: #3a3a3a;
    --on-band: #ffffff;
    --rule: #6b6f75;
  }
  * { box-sizing: border-box; margin: 0; padding: 0; }
  html, body {
    width: 1200px; height: 1000px; overflow: hidden;
    background: var(--page-bg);
  }
  .canvas { position: relative; width: 1200px; height: 1000px; }
  .banner {
    position: absolute; left: 420px; top: 89px;
    width: 360px; height: 856px; overflow: hidden;
    background: linear-gradient(160deg, var(--banner-top) 0%, var(--banner-mid) 45%, var(--banner-low) 100%);
    color: var(--ink);
    font-family: "Questrial", "Century Gothic", sans-serif;
  }
  .brand { position: absolute; top: 22px; left: 0; width: 100%; text-align: center; }
  .brand-name {
    font-family: "Montserrat", sans-serif; font-weight: 700;
    font-size: 34px; letter-spacing: 3px; line-height: 40px; color: var(--ink);
  }
  .brand-rule { width: 124px; height: 1px; background: var(--rule); margin: 3px auto 6px; }
  .brand-tag { font-size: 15px; letter-spacing: 1px; }
  .model-photo {
    position: absolute; left: 0; top: 95px; width: 262px; height: 420px;
    background: radial-gradient(ellipse at 55% 35%, #c9a8a0 0%, #8a7e86 35%, #e6e6ea 70%, #cfd5dc 100%);
    border-radius: 0 120px 0 0;
    opacity: .9;
  }
  .band {
    position: absolute; left: 0; width: 100%;
    background: linear-gradient(170deg, var(--band) 0%, var(--band) 55%, var(--band-sheen) 70%, var(--band) 85%);
    color: var(--on-band); text-align: center;
  }
  .headline-band { top: 515px; height: 52px; }
  .headline {
    font-family: "Montserrat", sans-serif; font-weight: 700;
    font-size: 25px; line-height: 52px; letter-spacing: .5px;
  }
  .url-band { top: 806px; height: 32px; }
  .url { font-size: 22px; line-height: 32px; letter-spacing: .5px; }
  .details { position: absolute; left: 20px; top: 570px; width: 330px; }
  .label { font-weight: 700; font-family: "Montserrat", sans-serif; font-size: 14px; }
  .services-title { font-size: 15px; }
  .service-cols { display: flex; gap: 0; margin-top: 1px; }
  .service-list { list-style: none; width: 130px; font-size: 14px; line-height: 16.4px; }
  .service-list li::before { content: "•"; }
  .contact { margin-top: 10px; font-size: 14px; line-height: 16px; }
  .email { margin-top: 10px; font-size: 14px; }
</style>
</head>
<body>
<div class="canvas">
  <section class="banner">
    <header class="brand">
      <div class="brand-name">VELUMO</div>
      <div class="brand-rule"></div>
      <div class="brand-tag">GÖZƏLLİK</div>
    </header>

    <div class="model-photo" role="img" aria-label="Fashion portrait of a woman with a sculpted updo, bold purple and green eye makeup and a white lace-trimmed blouse"></div>

    <div class="band headline-band"><p class="headline">Gözəllik hər yandadır...</p></div>

    <div class="details">
      <p class="label services-title">Services:</p>
      <div class="service-cols">
        <ul class="service-list">
          <li>Hair removal</li><li>Massage</li><li>Facials</li><li>Manicures</li>
          <li>Pedicures</li><li>Nails</li><li>Waxing</li><li>Threading</li>
        </ul>
        <ul class="service-list">
          <li>Hair removal</li><li>Massage</li><li>Facials</li><li>Manicures</li>
          <li>Pedicures</li><li>Nails</li><li>Waxing</li><li>Threading</li>
        </ul>
      </div>
      <div class="contact">
        <p class="label">Phone numbers:</p>
        <p>(012) 555 0142 • (051) 555 0187</p>
        <p>(055) 555 0163 • (070) 555 0129</p>
      </div>
      <p class="email"><span class="label">Email:</span> office@velumogozellik.com</p>
    </div>

    <div class="band url-band"><p class="url">www.velumogozellik.com</p></div>
  </section>
</div>
</body>
</html>
```